KRANO study results infographic

We enjoyed the previous infographic design you provided for us (The GaRVU cohort study Infographic), and would like to invite you to design another infographic in a similar style and layout.
We need an infographic which presents the results from the KRANO research trial. It should be colourful and engaging, in understandable language and showing the steps to get to the results. This is to showcase the results to patients/the public/clinicians, giving a brief summary of what the study proved. The final design should have the KRANO logo at the top (please see attached and https://krano.pelbu.quenmarsh.example/welcome-krano-trial)
I have attached the required logos which need to be used (KRANO, Penhallow Injury and Acute Care, University of Castlemere) as well as an example from another study, The GaRVU cohort study Infographic, as an example of what the layout could look like. Please DO NOT use the content from the The GaRVU cohort study Infographic example though, please instead use the content from the attached document 'KRANO_InfographicDesignInformation_Plinthwork'.

```html
<!DOCTYPE html>
<html lang="en">
<head>
<meta charset="utf-8">
<title>KRANO study results infographic</title>
<link href="https://fonts.googleapis.com/css2?family=Poppins:wght@400;500;600;700;800&display=swap" rel="stylesheet">
<style>
:root{
  --navy:#1d3461;
  --navy-deep:#172a52;
  --cyan:#1fa6df;
  --cyan-light:#5cc4ee;
  --teal:#2a9d8f;
  --band:#d9ecf8;
  --pale:#f2f8fc;
  --alert:#e4572e;
  --stage:#e6eaef;
  --white:#ffffff;
}
*{box-sizing:border-box;margin:0;padding:0}
html,body{width:1200px;height:1026px;overflow:hidden;background:var(--stage);font-family:"Poppins",Arial,sans-serif}
.poster{position:absolute;left:238px;top:0;width:724px;height:1026px;background:var(--white);overflow:hidden}
.header-shape{position:absolute;left:0;top:0;width:724px;height:272px}
.brand{position:absolute;left:0;top:34px;width:724px;display:flex;justify-content:center;align-items:center;gap:10px}
.brand-dot{width:22px;height:22px;border-radius:50%;background:var(--cyan)}
.brand-name{color:var(--white);font-weight:700;font-size:30px;letter-spacing:2px}
.title{position:absolute;left:0;top:118px;width:724px;text-align:center;color:var(--white);font-weight:800;font-size:25px;line-height:30px;text-transform:uppercase}
.subtitle{position:absolute;left:0;top:182px;width:724px;text-align:center;color:var(--cyan);font-weight:700;font-size:17px;line-height:22px;text-transform:uppercase}
.tag{position:absolute;background:var(--teal);color:var(--white);font-weight:700;font-size:17px;padding:0 10px;height:26px;line-height:26px;border-radius:2px;white-space:nowrap}
.eligibility-text{position:absolute;left:36px;top:322px;width:440px;padding-left:14px;border-left:5px solid var(--cyan);color:var(--navy);font-weight:700;font-size:17.5px;line-height:23px}
.art{position:absolute;border-radius:10px}
.methods-band{position:absolute;left:0;top:402px;width:724px;height:150px;background:var(--band)}
.count{position:absolute;left:134px;top:436px;color:var(--cyan);font-weight:800;font-size:64px;line-height:70px}
.count-label{position:absolute;left:134px;top:502px;color:var(--navy);font-weight:700;font-size:17px}
.methods-text{position:absolute;left:452px;top:428px;width:254px;color:var(--navy);font-size:18.5px;line-height:23px;font-weight:500}
.methods-text b{color:var(--cyan);font-weight:700}
.results-band{position:absolute;left:0;top:552px;width:724px;height:330px;background:var(--pale)}
.flow{position:absolute;left:0;top:0;width:724px;height:1026px}
.box{position:absolute;background:var(--cyan);color:var(--white);border-radius:6px;text-align:center;font-weight:700;font-size:12px;display:flex;flex-direction:column;justify-content:center;line-height:13px}
.box small{font-size:7px;font-weight:500;line-height:9px}
.box.step{font-size:13px}
.box.out{border:1.5px dashed var(--alert);background:var(--white);color:var(--alert)}
.box.rate{font-size:14px;line-height:15px}
.conclusion{position:absolute;left:33px;top:895px;width:360px;height:97px;background:var(--navy);border-radius:4px}
.conclusion-text{position:absolute;left:98px;top:925px;width:286px;color:var(--white);font-size:11.5px;line-height:15px;text-align:justify}
.funding{position:absolute;left:402px;top:893px;width:298px;color:var(--cyan);font-weight:700;font-size:12.5px;line-height:15px;text-align:justify}
.partners{position:absolute;left:402px;top:957px;width:310px;height:18px;display:flex;align-items:center;justify-content:space-between;white-space:nowrap}
.partner-name{color:var(--navy);font-weight:600;font-size:9px;line-height:16px;display:flex;align-items:center}
.partner-square{width:16px;height:16px;background:var(--navy);display:inline-block;margin-right:5px}
.contact{position:absolute;left:402px;top:979px;width:300px;color:var(--navy);font-size:6.5px;line-height:9px}
.footer-band{position:absolute;left:0;top:1010px;width:724px;height:16px;background:var(--navy)}
</style>
</head>
<body>
<main class="poster">
  <svg class="header-shape" viewBox="0 0 724 272" aria-hidden="true">
    <polygon points="0,0 724,0 724,262 0,212" fill="var(--navy)"/>
    <polygon points="0,212 724,262 724,272 0,220" fill="var(--cyan)"/>
  </svg>
  <div class="brand"><span class="brand-dot"></span><span class="brand-name">KRANO</span></div>
  <h1 class="title">Standard dressing versus negative pressure<br>wound therapy</h1>
  <p class="subtitle">A treatment of surgical incisions for hip fracture</p>

  <div class="tag" style="left:33px;top:288px">Eligibility</div>
  <p class="eligibility-text">Inclusion: ≥65 years, any hip fracture surgery. Exclusion: undisplaced intracapsular fractures with screws or other barriers.</p>
  <div class="art" role="img" aria-label="Illustration of a carer pushing an older patient in a wheelchair" style="left:493px;top:276px;width:195px;height:120px;background:linear-gradient(135deg,#f3c66a,#2c4f8c)"></div>

  <section class="methods-band"></section>
  <div class="tag" style="left:33px;top:408px">Methods</div>
  <div class="art" role="img" aria-label="Illustration of an older person with a walking frame" style="left:36px;top:438px;width:80px;height:103px;background:linear-gradient(180deg,#f2b441,#7d7f86)"></div>
  <div class="count">462</div>
  <div class="count-label">Participants</div>
  <div class="art" role="img" aria-label="Illustration of a hospital building" style="left:280px;top:450px;width:146px;height:91px;background:linear-gradient(180deg,#8fd0f0,#4aa96c)"></div>
  <p class="methods-text"><b>&gt;65 years</b> undergoing hip fracture surgery at <b>5 UK center</b>, deep SSI rate was access at 30 &amp; 90 days</p>

  <section class="results-band"></section>
  <div class="tag" style="left:33px;top:558px">Results</div>
  <div class="art" role="img" aria-label="Illustration of a doctor talking with a worried patient" style="left:544px;top:548px;width:156px;height:97px;background:linear-gradient(135deg,#e05a4f,#34558f)"></div>
  <div class="art" role="img" aria-label="Illustration of a nurse holding a clipboard" style="left:51px;top:730px;width:52px;height:140px;background:linear-gradient(180deg,#f2b441,#5b7fc4)"></div>

  <svg class="flow" viewBox="0 0 724 1026" aria-hidden="true" fill="none" stroke="var(--cyan)" stroke-width="1.5">
    <path d="M298 579H335M413 579H450M374 591V605M335 617H298M374 629V641M374 664V674M257 674H491M257 674V684M491 674V684"/>
    <path d="M257 706V720M216 732H198M257 745V757M257 781V794M257 815V826M163 826H304M163 826V837M304 826V837"/>
    <path d="M491 706V720M532 732H544M491 745V757M491 781V794M491 815V826M445 826H586M445 826V837M586 826V837"/>
  </svg>

  <div class="box step" style="left:216px;top:568px;width:82px;height:22px">Enrolment</div>
  <div class="box" style="left:335px;top:567px;width:78px;height:24px">n = 945<small>Eligibility Assessment</small></div>
  <div class="box out" style="left:450px;top:567px;width:79px;height:24px">n = 478<small>Excluded</small></div>
  <div class="box out" style="left:216px;top:605px;width:82px;height:25px">n = 02<small>Randomized in error</small></div>
  <div class="box" style="left:335px;top:605px;width:78px;height:24px">n = 467<small>Randomized</small></div>
  <div class="box step" style="left:332px;top:641px;width:85px;height:23px">Allocation</div>
  <div class="box step" style="left:216px;top:684px;width:82px;height:22px">Standard</div>
  <div class="box step" style="left:450px;top:684px;width:82px;height:22px">iNPWT</div>
  <div class="box out" style="left:119px;top:720px;width:79px;height:25px">n = 03<small>Not Allocated</small></div>
  <div class="box" style="left:216px;top:720px;width:82px;height:25px">n = 232<small>Allocated</small></div>
  <div class="box" style="left:450px;top:720px;width:82px;height:25px">n = 217<small>Allocated</small></div>
  <div class="box out" style="left:544px;top:720px;width:76px;height:25px">n = 16<small>Not Allocated</small></div>
  <div class="box" style="left:216px;top:757px;width:82px;height:24px">n = 218<small>Completed 30 Days</small></div>
  <div class="box" style="left:450px;top:757px;width:82px;height:24px">n = 214<small>Completed 30 Days</small></div>
  <div class="box step" style="left:216px;top:794px;width:82px;height:21px">Deep SSI</div>
  <div class="box step" style="left:450px;top:794px;width:82px;height:21px">Deep SSI</div>
  <div class="box rate" style="left:119px;top:837px;width:88px;height:29px">6.4 %<small>After 30 days</small></div>
  <div class="box rate" style="left:262px;top:837px;width:85px;height:29px">6.4 %<small>After 90 days</small></div>
  <div class="box rate" style="left:403px;top:837px;width:85px;height:29px">1.9 %<small>After 30 days</small></div>
  <div class="box rate" style="left:544px;top:837px;width:85px;height:29px">2.3 %<small>After 90 days</small></div>

  <section class="conclusion"></section>
  <div class="tag" style="left:33px;top:893px;height:24px;line-height:24px">Conclusion</div>
  <div class="art" role="img" aria-label="Icon of a group of people" style="left:44px;top:930px;width:46px;height:40px;border-radius:6px;background:linear-gradient(180deg,#ffffff,#9fd6f2)"></div>
  <p class="conclusion-text">The rate of deep SSI 30 days after sugery for a fracture of the hip was 4%, which makes a study comparing the clinical effectiveness of standard dressings and iNPWT feasible.</p>

  <p class="funding">This study funded by: Brackenfield College of Surgeons/Ashgrove Medical Trust, Castlemere Biomedical Research Centre, Ferrow &amp; Lane.</p>
  <div class="partners">
    <span class="partner-name">Penhallow Injury and Acute Care</span>
    <span class="partner-name"><span class="partner-square"></span>University of Castlemere</span>
  </div>
  <p class="contact">Chief Investigator: Tamsin Orrell — tamsin.orrell@pelbu.example<br>krano.pelbu.quenmarsh.example</p>
  <div class="footer-band"></div>
</main>
</body>
</html>
```